Radon Reduction & Mold Removal Website

I need you to set up a WordPress account for me and design a full width, professional-looking, mobile-responsive website for my business. We offer radon reduction and mold removal (two household environmental issues).
We have merged 2 companies and need a single website to promote both services (radon and mold). Here are the current websites from the 2 businesses that have merged:
RADON
http://klendor-airfix.com/
MOLD
http://brisketfungusclear.net/
Once complete, I will need the login to the WordPress account so I have access to the site to make changes, additions, and modifications.
Target Market(s)
Home Owners
Industry/Entity Type
Home And Garden
Look and feel
Each slider illustrates characteristics of the customer's brand and the style your logo design should communicate.

```html
<!DOCTYPE html>
<html lang="en">
<head>
<meta charset="utf-8">
<title>Klendor Clearway – Radon Reduction & Mold Removal</title>
<link rel="stylesheet" href="https://fonts.googleapis.com/css2?family=Roboto:wght@400;500;700&display=swap">
<style>
:root{
  --black:#000;
  --ink:#111;
  --white:#fff;
  --yellow:#f4f27a;
  --brand-yellow:#f2e81c;
  --grey-card:#eeeeee;
  --text-grey:#666;
  --footer-text:#cfcfcf;
  --bar:#0c0c0c;
  --rule:#d9d9d9;
}
*{box-sizing:border-box;margin:0;padding:0}
html,body{width:769px;height:1200px;overflow:hidden}
body{font-family:"Roboto",Arial,sans-serif;background:var(--white);color:var(--ink);position:relative}

/* header */
.site-header{position:absolute;left:0;top:0;width:769px;height:76px;background:var(--black)}
.brand{position:absolute;left:55px;top:26px;display:flex;align-items:center;gap:7px;color:var(--brand-yellow);font-weight:700;font-size:14px;letter-spacing:.4px}
.brand-mark{width:12px;height:12px;background:var(--brand-yellow)}
.main-nav{position:absolute;top:34px;left:0;font-size:8px;font-weight:500;color:var(--white);letter-spacing:.2px}
.main-nav a{position:absolute;white-space:nowrap;color:inherit;text-decoration:none}
.btn-signup{position:absolute;left:556px;top:28px;width:55px;height:20px;border-radius:5px;background:var(--yellow);color:var(--ink);font-size:8px;font-weight:500;display:flex;align-items:center;justify-content:center}
.search{position:absolute;left:619px;top:28px;width:94px;height:20px;border-radius:4px;background:var(--white);font-size:7px;color:#999;padding:6px 8px;letter-spacing:.3px}
.search svg{position:absolute;right:6px;top:5px}

/* hero */
.hero{position:absolute;left:0;top:76px;width:769px;height:336px;
  background:linear-gradient(180deg,#1f2a22 0%,#3a3f33 18%,#7d7a62 40%,#8a8870 58%,#4d5a3a 78%,#3f6a2a 100%)}
.hero-arrow{position:absolute;top:156px;width:25px;height:25px;border:2px solid var(--white);border-radius:50%;display:flex;align-items:center;justify-content:center}

/* about */
.about-title{position:absolute;left:0;top:441px;width:769px;text-align:center;font-size:18px;font-weight:500;color:var(--ink)}
.about-text{position:absolute;left:160px;top:466px;width:449px;text-align:center;font-size:7.5px;line-height:13px;color:var(--text-grey);text-transform:uppercase;letter-spacing:.2px}

/* service cards */
.service-card{position:absolute;top:535px;width:156px;height:200px;background:var(--grey-card);text-align:center}
.service-card.is-active{background:var(--black)}
.service-icon{position:absolute;left:31px;top:13px;width:94px;height:94px;border-radius:50%;background:var(--black);display:flex;align-items:center;justify-content:center}
.is-active .service-icon{background:var(--white)}
.service-title{position:absolute;left:0;top:112px;width:156px;font-size:9.5px;font-weight:500;color:#555}
.is-active .service-title{color:var(--white);font-weight:700}
.service-text{position:absolute;left:14px;top:127px;width:128px;font-size:7.5px;line-height:11px;color:#666;text-transform:uppercase}
.is-active .service-text{color:var(--white)}
.service-more{position:absolute;left:51px;top:168px;width:54px;height:19px;border-radius:4px;background:var(--black);color:var(--white);font-size:8px;font-weight:700;display:flex;align-items:center;justify-content:center}
.is-active .service-more{background:var(--white);color:var(--ink)}

.divider{position:absolute;left:55px;top:767px;width:658px;height:1px;background:var(--rule)}

/* products */
.product-title{position:absolute;top:800px;font-size:12.5px;font-weight:700;color:var(--ink);white-space:nowrap}
.product-photo{position:absolute;top:823px;width:209px;height:161px}
.photo-fan{background:linear-gradient(135deg,#4a5366,#8a909c 55%,#3b4252)}
.photo-attic{background:linear-gradient(160deg,#9c6a3c,#c49766 45%,#e8e2dc 80%)}
.photo-water{background:linear-gradient(135deg,#b38a5c,#c9a47a 50%,#8c6b48)}

/* footer */
.site-footer{position:absolute;left:0;top:1016px;width:769px;height:184px;background:var(--black);color:var(--footer-text)}
.footer-heading{position:absolute;top:16px;font-size:13.5px;font-weight:500;color:var(--white);white-space:nowrap}
.footer-rule{position:absolute;top:37px;width:101px;height:2px;background:var(--yellow)}
.contact-row{position:absolute;left:55px;font-size:7.5px;line-height:11px;text-transform:uppercase;display:flex;gap:8px}
.contact-row svg{flex:none;margin-top:1px}
.footer-nav{position:absolute;left:209px;top:52px;font-size:7.5px;line-height:11.5px;text-transform:uppercase}
.footer-nav a{display:block;color:var(--footer-text);text-decoration:underline}
.social{position:absolute;left:206px;top:121px;display:flex;gap:5px}
.social span{width:22px;height:22px;border-radius:50%;background:#9a9a9a}
.post{position:absolute;left:360px;display:flex;gap:10px;font-size:7.5px;line-height:14px;text-transform:uppercase;width:200px}
.post-thumb{flex:none;width:35px;height:33px;background:linear-gradient(135deg,#6a7a92,#b08a6a)}
.news-input{position:absolute;left:593px;width:120px;height:21px;border-radius:5px;background:#e4e4e4;font-size:7.5px;color:#777;padding:6px 10px}
.news-btn{position:absolute;left:593px;top:106px;width:37px;height:21px;border-radius:4px;background:var(--yellow);color:var(--ink);font-size:8px;font-weight:500;display:flex;align-items:center;justify-content:center}
.footer-bar{position:absolute;left:0;top:161px;width:769px;height:23px;background:var(--bar);border-top:1px solid #2a2a2a;font-size:6.5px;color:var(--footer-text);text-transform:uppercase}
.footer-bar .copy{position:absolute;left:55px;top:8px}
.footer-bar .legal{position:absolute;right:56px;top:8px}
</style>
</head>
<body>

<header class="site-header">
  <div class="brand"><span class="brand-mark"></span>KLENDOR CLEARWAY</div>
  <nav class="main-nav">
    <a style="left:248px">HOME</a>
    <a style="left:291px">SERVICES</a>
    <a style="left:348px">PRODUCTS</a>
    <a style="left:407px">GET A QUOTE</a>
    <a style="left:473px">CONTACT US</a>
  </nav>
  <div class="btn-signup">SIGN UP</div>
  <div class="search">SEARCH
    <svg width="10" height="10" viewBox="0 0 10 10"><circle cx="4" cy="4" r="3" fill="none" stroke="#aaa" stroke-width="1.2"/><line x1="6.2" y1="6.2" x2="9" y2="9" stroke="#aaa" stroke-width="1.2"/></svg>
  </div>
</header>

<section class="hero" role="img" aria-label="Two-storey suburban home with olive siding, white trim and a landscaped green lawn at dusk">
  <div class="hero-arrow" style="left:55px"><svg width="10" height="10" viewBox="0 0 10 10"><path d="M6.5 1.5 3 5l3.5 3.5" fill="none" stroke="#fff" stroke-width="1.6"/></svg></div>
  <div class="hero-arrow" style="left:687px"><svg width="10" height="10" viewBox="0 0 10 10"><path d="M3.5 1.5 7 5 3.5 8.5" fill="none" stroke="#fff" stroke-width="1.6"/></svg></div>
</section>

<h1 class="about-title">ABOUT US</h1>
<p class="about-text">Lorem Ipsum is simply dummy text of the printing and typesetting industry. Lorem Ipsum has been the industry's standard dummy text ever since the 1500s, when an unknown printer took a galley of type and scrambled it to make a type specimen book.</p>

<article class="service-card is-active" style="left:55px">
  <div class="service-icon">
    <svg width="44" height="38" viewBox="0 0 44 38"><path d="M22 2 2 19h6v17h11V25h6v11h11V19h6z" fill="#000"/><rect x="31" y="5" width="5" height="9" fill="#000"/></svg>
  </div>
  <h2 class="service-title">RESIDENTIAL SERVICES</h2>
  <p class="service-text">Lorem Ipsum is simply dummy text of the printing and type-setting industry.</p>
  <div class="service-more">MORE</div>
</article>

<article class="service-card" style="left:221px">
  <div class="service-icon">
    <svg width="40" height="40" viewBox="0 0 40 40"><path d="M8 18a12 12 0 0 1 24 0z" fill="#fff"/><rect x="5" y="18" width="30" height="3" fill="#fff"/><path d="M8 40v-8a12 8 0 0 1 24 0v8z" fill="#fff"/></svg>
  </div>
  <h2 class="service-title">RESIDENTIAL SERVICES</h2>
  <p class="service-text">Lorem Ipsum is simply dummy text of the printing and type-setting industry.</p>
  <div class="service-more">MORE</div>
</article>

<article class="service-card" style="left:391px">
  <div class="service-icon">
    <svg width="36" height="40" viewBox="0 0 36 40"><rect x="4" y="3" width="24" height="32" fill="none" stroke="#fff" stroke-width="2.5"/><g stroke="#fff" stroke-width="2"><line x1="9" y1="11" x2="23" y2="11"/><line x1="9" y1="17" x2="23" y2="17"/><line x1="9" y1="23" x2="18" y2="23"/></g><circle cx="27" cy="31" r="7" fill="#fff"/><path d="m23.5 31 2.5 2.5 4.5-5" fill="none" stroke="#000" stroke-width="2"/></svg>
  </div>
  <h2 class="service-title">RESIDENTIAL SERVICES</h2>
  <p class="service-text">Lorem Ipsum is simply dummy text of the printing and type-setting industry.</p>
  <div class="service-more">MORE</div>
</article>

<article class="service-card" style="left:557px">
  <div class="service-icon">
    <svg width="40" height="40" viewBox="0 0 40 40"><rect x="6" y="4" width="22" height="14" rx="2" fill="none" stroke="#fff" stroke-width="2.2"/><text x="17" y="15" fill="#fff" font-family="Roboto,Arial,sans-serif" font-size="11" font-weight="700" text-anchor="middle">$</text><path d="M8 38V28l11-8 11 8v10z" fill="#fff"/><rect x="16" y="30" width="6" height="8" fill="#000"/></svg>
  </div>
  <h2 class="service-title">RESIDENTIAL SERVICES</h2>
  <p class="service-text">Lorem Ipsum is simply dummy text of the printing and type-setting industry.</p>
  <div class="service-more">MORE</div>
</article>

<div class="divider"></div>

<h3 class="product-title" style="left:55px">INLINE DRAFTLINE FAN</h3>
<div class="product-photo photo-fan" style="left:55px" role="img" aria-label="Inline radon fan mounted on white vertical piping"></div>
<h3 class="product-title" style="left:279px">INTERIOR AND GARAGE</h3>
<div class="product-photo photo-attic" style="left:279px" role="img" aria-label="Radon fan installed in an attic above insulation"></div>
<h3 class="product-title" style="left:503px">RADON WATER SYSTEMS</h3>
<div class="product-photo photo-water" style="left:503px" role="img" aria-label="Exterior radon pipe against a brick wall on a deck"></div>

<footer class="site-footer">
  <h4 class="footer-heading" style="left:55px">CONTACT US</h4>
  <div class="footer-rule" style="left:55px"></div>
  <div class="contact-row" style="top:55px">
    <svg width="8" height="10" viewBox="0 0 8 10"><path d="M4 0a3.5 3.5 0 0 0-3.5 3.5C.5 6 4 10 4 10s3.5-4 3.5-6.5A3.5 3.5 0 0 0 4 0z" fill="#cfcfcf"/><circle cx="4" cy="3.5" r="1.3" fill="#000"/></svg>
    <span>41 Harlow Ave Ste 300<br>Brenford,<br>IL 60999-0142</span>
  </div>
  <div class="contact-row" style="top:99px">
    <svg width="9" height="9" viewBox="0 0 9 9"><path d="M1.8.5 3.4 2.6 2.5 3.7a5.5 5.5 0 0 0 2.8 2.8l1.1-.9 2.1 1.6-.9 1.3C4.7 8.5.5 4.3.5 1.4z" fill="#cfcfcf"/></svg>
    <span>1-800-555-0148</span>
  </div>
  <div class="contact-row" style="top:117px">
    <svg width="9" height="7" viewBox="0 0 9 7"><rect width="9" height="7" fill="#cfcfcf"/><path d="m0 0 4.5 3.5L9 0" fill="none" stroke="#000" stroke-width=".8"/></svg>
    <span>HELLO@KLENDORCLEARWAY.COM</span>
  </div>

  <h4 class="footer-heading" style="left:209px">NAVIGATION</h4>
  <div class="footer-rule" style="left:209px"></div>
  <nav class="footer-nav">
    <a>Home</a><a>Service</a><a>Product</a><a>Get a Quote</a><a>Contact Us</a>
  </nav>
  <div class="social" aria-label="Social links"><span></span><span></span><span></span></div>

  <h4 class="footer-heading" style="left:360px">RECENT POST</h4>
  <div class="footer-rule" style="left:360px"></div>
  <div class="post" style="top:57px"><div class="post-thumb" role="img" aria-label="Post thumbnail"></div><span>Lakeshore Valley Estate Auctioneers Guild</span></div>
  <div class="post" style="top:108px"><div class="post-thumb" role="img" aria-label="Post thumbnail"></div><span>Lakeshore Valley Estate Auctioneers Guild</span></div>

  <h4 class="footer-heading" style="left:593px">NEWS LATTER</h4>
  <div class="footer-rule" style="left:593px"></div>
  <div class="news-input" style="top:50px">NAME</div>
  <div class="news-input" style="top:79px">EMAIL</div>
  <div class="news-btn">SIGN UP</div>

  <div class="footer-bar">
    <span class="copy">Copyright © 2015 Radon Mitigation | Klendor Clearway Mitigation Services</span>
    <span class="legal">Terms of Use &nbsp;/&nbsp; Privacy Policy &nbsp;/&nbsp; Directory</span>
  </div>
</footer>

</body>
</html>
```